National Dance Competition Needs a Program Cover Design

We need a program cover design for our 2017 season programs. Program size is standard 8.5" x 11", full color. The only required elements to include in the design are the Stellar Step Showcase logo (see uploaded file), and the copy: "2017 Regional Competition" and "20th Anniversary Season". All other design elements are per the creative mind of the designer. Logo can be "embellished" if that's the direction the design leads. This is a children's dance competition (ages 5-19) so design should be colorful, fun, and exciting. The winning design will likely be the springboard to other projects including designs for awards plaques, trophy mylars, and program ads. We are looking to establish an ongoing relationship with a designer. For more information about us go to www.stellarstepshowcase.example.

Target Market(s)

Dancers ages 5-19, their parents and dance instructors

Requirements
Must have
• See project description above
Should not have
• Do not fall into the mindset that dance is Ballet only. Our kids also compete in Jazz, Tap, Lyrical, Contemporary, Hip Hop and many other styles.

```html
<!DOCTYPE html>
<html lang="en">
<head>
<meta charset="utf-8">
<title>Stellar Step Showcase – 2017 Regional Competition Program Cover</title>
<link rel="stylesheet" href="https://fonts.googleapis.com/css2?family=Righteous&family=Roboto+Condensed:wght@700&display=swap">
<style>
  :root {
    --page-bg: #2b2b2d;
    --violet-deep: #3a0f6e;
    --violet: #6a1fa8;
    --violet-bright: #9b3fd6;
    --magenta: #d65ef0;
    --glow: #f4eefc;
    --glow-green: #c9f0a0;
    --teal: #1e9aa6;
    --red: #c4102e;
    --navy: #2a2a8a;
    --band: #5a1a90;
    --band-light: #8a40c0;
    --paper: #e9e6ee;
    --white: #ffffff;
  }
  * { margin: 0; padding: 0; box-sizing: border-box; }
  html, body {
    width: 1134px; height: 1200px; overflow: hidden;
    background: var(--page-bg);
  }
  .program-cover {
    position: absolute; left: 134px; top: 40px;
    width: 866px; height: 1120px; overflow: hidden;
    background:
      radial-gradient(ellipse 420px 300px at 460px 280px, var(--glow) 0%, rgba(230,210,250,.85) 30%, rgba(150,80,210,0) 75%),
      radial-gradient(ellipse 260px 200px at 430px 540px, rgba(201,240,160,.8) 0%, rgba(201,240,160,0) 70%),
      linear-gradient(180deg, var(--violet) 0%, var(--violet-bright) 45%, var(--violet) 100%);
  }
  .stage-crowd {
    position: absolute; left: 0; top: 630px; width: 866px; height: 440px;
    background:
      radial-gradient(ellipse 380px 200px at 560px 250px, rgba(240,140,250,.95) 0%, rgba(214,94,240,.6) 45%, rgba(214,94,240,0) 100%),
      linear-gradient(180deg, rgba(80,20,130,0) 0%, rgba(80,20,130,.75) 30%, rgba(110,30,160,.9) 100%);
  }
  .brand-name {
    position: absolute; left: 0; right: 0; top: 130px;
    text-align: center;
    font-family: "Righteous", sans-serif; font-weight: 400;
    font-size: 66px; line-height: 1.05;
    color: var(--teal);
  }
  .season-year {
    position: absolute; left: 0; right: 0; top: 345px;
    text-align: center;
    font-family: "Roboto Condensed", sans-serif; font-weight: 700;
    font-size: 190px; line-height: 1; letter-spacing: -2px;
    color: var(--red);
  }
  .event-title {
    position: absolute; left: 0; right: 0; top: 555px;
    text-align: center;
    font-family: "Righteous", sans-serif; font-weight: 400;
    color: var(--navy);
    line-height: 1;
  }
  .event-title .line-regional { display: block; font-size: 96px; }
  .event-title .line-competition { display: block; font-size: 104px; margin-top: 6px; }
  .cover-bands { position: absolute; left: 0; top: 0; }
  .anniversary {
    position: absolute; left: 240px; top: 965px; width: 560px;
    text-align: center;
    font-family: "Righteous", sans-serif; font-weight: 400;
    font-size: 40px; line-height: 1;
    color: var(--white);
    transform: rotate(16.95deg);
    transform-origin: center;
  }
</style>
</head>
<body>
  <main class="program-cover">
    <div class="stage-crowd" role="img" aria-label="Silhouettes of dancers performing on a glowing dotted dance floor"></div>

    <h1 class="brand-name">Stellar Step<br>Showcase</h1>
    <p class="season-year">2017</p>
    <h2 class="event-title">
      <span class="line-regional">REGIONAL</span>
      <span class="line-competition">COMPETITION</span>
    </h2>

    <svg class="cover-bands" width="866" height="1120" viewBox="0 0 866 1120" aria-hidden="true">
      <polygon points="0,736 866,1000 866,1120 0,1120" fill="var(--band)" opacity=".92"/>
      <polygon points="0,736 866,1000 866,1014 0,752" fill="var(--band-light)" opacity=".7"/>
      <polygon points="0,895 650,1120 0,1120" fill="var(--paper)"/>
      <polygon points="130,1120 200,1072 300,1072 420,1120" fill="var(--band)"/>
    </svg>

    <p class="anniversary">20th Anniversary Season</p>
  </main>
</body>
</html>
```